E-mail Ad Design Project

I would like a lower banner ad designed for placement within an e-mail. The size has to be 450px x 230px (6in x 3.07in) and must be either a GIF or JPEG, not to exceed 30K.

We are a medical billing company that provides services to physical therapy practices in Florida, and this ad is intended for owners and office managers of physical therapy businesses. We provide therapy offices with practice management software, submit medical claims on behalf of their patients, follow-up with insurance companies on outstanding claims, and also perform necessary back-end collections with patient balances. We also are able to interface with popular therapy documentation products to streamline data entry.

The design colors should incorporate our logo and red/blue colors (see www.clinicianharbor.net).

Target Market(s)

Physical therapists and administrators of physical therapy offices

Industry/Entity Type

Physical Therapy

Requirements
Must have
• Grabbing/heading text:

Tired of Denials and Confusing Rejection Codes?
We Take the Pain Out of Medical Billing.

Offer:

Get Started Today with 2 Free Months of Billing
Nice to have
• We provide services mainly to Florida therapists, so it would be nice to have an image or text that highlights this fact. Also, the e-mail campaign this is a part of will be sent to Florida recipients.

```html
<!DOCTYPE html>
<html lang="en">
<head>
<meta charset="utf-8">
<title>Clinician Harbor – Medical Billing Banner</title>
<link rel="stylesheet" href="https://fonts.googleapis.com/css2?family=Arimo:ital,wght@0,700;1,700&display=swap">
<style>
  :root {
    --navy: #1b2a5c;
    --navy-deep: #111c44;
    --swoosh: #3f6fb8;
    --swoosh-light: #9fb9e0;
    --white: #ffffff;
    --red: #d8241c;
    --red-dark: #9e130e;
    --gold: #f2c14a;
    --button-top: #4aa3ea;
    --button-bottom: #0e5aa8;
    --ink-grey: #333a48;
    --footer: #e6e8ec;
  }
  html, body { margin: 0; padding: 0; overflow: hidden; background: var(--white); }
  .banner {
    position: relative;
    width: 1200px; height: 613px;
    overflow: hidden;
    background: var(--white);
    font-family: "Arimo", Arial, sans-serif;
  }
  .header-band { position: absolute; left: 0; top: 0; width: 1200px; height: 190px; }
  .header-title {
    position: absolute; right: 24px; top: 24px; margin: 0;
    color: var(--white); font-style: italic; font-weight: 700;
    font-size: 46px; letter-spacing: 0.2px;
  }
  .team-photo {
    position: absolute; left: 650px; top: 150px; width: 550px; height: 463px;
    background: linear-gradient(160deg, #dfe7f0 0%, #f4f6f8 45%, #c9d6e4 100%);
  }
  .headline { position: absolute; left: 0; top: 0; margin: 0; color: var(--navy);
    font-weight: 700; font-size: 50px; line-height: 1; text-transform: uppercase; }
  .headline span { position: absolute; white-space: nowrap; }
  .headline .l1 { left: 48px; top: 165px; }
  .headline .l2 { left: 410px; top: 220px; }
  .headline .l3 { left: 458px; top: 275px; }
  .offer-badge { position: absolute; left: 60px; top: 210px; width: 260px; height: 260px; }
  .cta-button {
    position: absolute; left: 27px; top: 428px; width: 398px; height: 98px;
    box-sizing: border-box; border-radius: 16px;
    border: 4px solid #0a3f7c;
    background: linear-gradient(var(--button-top), var(--button-bottom));
    color: var(--white); font-weight: 700; font-size: 44px;
    display: flex; align-items: center; justify-content: center;
    text-decoration: none; box-shadow: 0 4px 8px rgba(0,0,0,0.3);
  }
  .footer-bar { position: absolute; left: 0; top: 545px; width: 650px; height: 68px; background: var(--footer); }
  .brand-name {
    position: absolute; left: 24px; top: 560px; margin: 0;
    color: var(--ink-grey); font-weight: 700; font-size: 30px; letter-spacing: 1px;
    text-transform: uppercase;
  }
</style>
</head>
<body>
<div class="banner">
  <div class="team-photo" role="img" aria-label="Photo of a physician and a nurse reviewing billing on a computer screen"></div>

  <svg class="header-band" viewBox="0 0 1200 190" aria-hidden="true">
    <path d="M0 0 H1200 V70 C900 100 500 130 0 112 Z" fill="var(--navy)"/>
    <path d="M0 112 C500 130 900 100 1200 70 V96 C900 135 500 165 0 140 Z" fill="var(--swoosh)"/>
    <path d="M0 140 C500 165 900 135 1200 96 V110 C900 155 500 185 0 160 Z" fill="var(--swoosh-light)"/>
  </svg>
  <h1 class="header-title">Tired of Denials &amp; Confusing Rejection Codes?</h1>

  <h2 class="headline">
    <span class="l1">We take the pain out</span>
    <span class="l2">of medical</span>
    <span class="l3">billing</span>
  </h2>

  <svg class="offer-badge" viewBox="0 0 260 260" aria-label="2 free months of billing">
    <polygon fill="var(--red)" points="130,5 146,30 172,12 179,42 210,35 206,66 236,70 220,97 248,112 224,132 248,150 220,164 236,192 206,195 210,226 179,219 172,249 146,232 130,256 114,232 88,249 81,219 50,226 54,195 24,192 40,164 12,150 36,132 12,112 40,97 24,70 54,66 50,35 81,42 88,12 114,30"/>
    <circle cx="130" cy="130" r="92" fill="none" stroke="var(--gold)" stroke-width="5"/>
    <circle cx="130" cy="130" r="84" fill="var(--red-dark)" opacity="0.25"/>
    <text x="130" y="128" text-anchor="middle" fill="var(--white)" font-family="Arimo, Arial, sans-serif" font-weight="700" font-size="82">2</text>
    <text x="130" y="165" text-anchor="middle" fill="var(--white)" font-family="Arimo, Arial, sans-serif" font-weight="700" font-size="27">free Months</text>
    <text x="130" y="194" text-anchor="middle" fill="var(--white)" font-family="Arimo, Arial, sans-serif" font-weight="700" font-size="24">of Billing</text>
  </svg>

  <a class="cta-button" href="#">Get Started NOW</a>

  <div class="footer-bar"></div>
  <p class="brand-name">Clinician Harbor</p>
</div>
</body>
</html>
```